Verpackungen für neue online Schokoladenmarke
Zielgruppe
Eine neue online Schokoladenmarke deren Zielgruppe sind anspruchsvolle Schokoladenliebhaber,
denn die Schokolade wird aus Kakaobohnen langzeitgewalzt.
Die Käufer essen nicht süß, sondern wünschen den wirklichen Kakaobohnengeschmack ohne
Zusatzstoffe.
Die Schokolade wird nur online verkauft.
Aufgabenstellung
Markenname: leaf9tin Chocolate ---------- oder----- LEAF9TIN Chocolate oder ?
Der Markenname soll dominant sein, und die Vorderseite eines Tafelkartons prägen, als
Umverpackung 80 x 160 mm - die Vorderseite, nur die ist hier beauftragt.
Obwohl Bio, muss die Verpackung nicht recycelt oder 'alternativ' aussehen, nicht im Öko - Design auftreten.
Bitte keine angebissenen Schokotafeln, Sahnetöpfe oder sonstige altmodischen Grafiken nutzen.
Der Firmenname leaf9tin soll (gut lesbar) gestaltet werden, in Groß- oder Kleinbuchstaben etc. Eventuell
einen Bezug auf Online haben, oder auch nicht...
Der Gewinner kann ggf. weitere Designaufträge und auch die Layouts bzw. Datenübergabe für den
Kartonhersteller machen. Dauerbetreuung erwünscht..!

```html
<!DOCTYPE html>
<html lang="de">
<head>
<meta charset="utf-8">
<title>leaf9tin Chocolate – Tafelkarton Vorderseite</title>
<link rel="stylesheet" href="https://fonts.googleapis.com/css2?family=Caveat:wght@600&family=Shrikhand&display=swap">
<style>
  :root {
    --page: #e8e6e3;
    --olive: #3c4a1d;
    --yolk: #f8b60e;
    --cream: #f6ebc9;
    --blush: #f1a9a6;
    --scarlet: #e2161b;
    --violet: #901b82;
    --cocoa: #b24e1c;
  }
  * { margin: 0; padding: 0; box-sizing: border-box; }
  html, body {
    width: 1200px;
    height: 1200px;
    overflow: hidden;
    background: var(--page);
  }
  .canvas {
    position: relative;
    width: 1200px;
    height: 1200px;
  }
  .carton-front {
    position: absolute;
    left: 320px;
    top: 40px;
    width: 560px;
    height: 1120px;
    background: var(--olive);
    overflow: hidden;
  }
  .product-title {
    position: absolute;
    left: 0;
    top: 70px;
    width: 100%;
    text-align: center;
    font-family: "Shrikhand", cursive;
    font-size: 86px;
    line-height: 1;
    letter-spacing: -3px;
    color: var(--yolk);
    transform: scaleY(1.7);
    transform-origin: top center;
  }
  .tagline {
    position: absolute;
    left: 60px;
    top: 320px;
    font-family: "Caveat", cursive;
    font-weight: 600;
    font-size: 40px;
    line-height: 1.05;
    color: var(--cream);
    transform: rotate(5deg);
    transform-origin: left top;
  }
  .tagline span { display: block; }
  .tagline span:first-child { padding-left: 18px; }
  .dancer-illustration {
    position: absolute;
    left: 90px;
    top: 500px;
    width: 400px;
    height: 580px;
  }
  .brand-name {
    position: absolute;
    left: 26px;
    top: 880px;
    font-family: "Shrikhand", cursive;
    font-size: 92px;
    line-height: 1;
    letter-spacing: -2px;
    color: var(--cream);
  }
  .claim {
    position: absolute;
    left: 50px;
    top: 1010px;
    font-family: "Caveat", cursive;
    font-weight: 600;
    font-size: 38px;
    color: var(--blush);
    transform: rotate(6deg);
    transform-origin: left top;
  }
  .organic-mark {
    position: absolute;
    left: 330px;
    top: 1050px;
    font-family: "Caveat", cursive;
    font-weight: 600;
    font-size: 36px;
    color: var(--blush);
    transform: rotate(6deg);
  }
</style>
</head>
<body>
<main class="canvas">
  <section class="carton-front">
    <h1 class="product-title">CHOCOLATE</h1>
    <p class="tagline"><span>Kakaobohnengeschmack</span><span>ohne Zusatzstoffe</span></p>

    <svg class="dancer-illustration" viewBox="0 0 400 580" role="img"
         aria-label="Illustration: tanzende Frau mit violettem Haar, rosa Oberteil und roter Hose, Arme erhoben">
      <defs>
        <linearGradient id="dancerTones" x1="0" y1="0" x2="0" y2="1">
          <stop offset="0" stop-color="var(--cocoa)"/>
          <stop offset="0.3" stop-color="var(--violet)"/>
          <stop offset="0.55" stop-color="var(--blush)"/>
          <stop offset="0.75" stop-color="var(--scarlet)"/>
          <stop offset="1" stop-color="var(--scarlet)"/>
        </linearGradient>
      </defs>
      <rect x="0" y="0" width="400" height="580" rx="60" fill="url(#dancerTones)" opacity="0.9"/>
    </svg>

    <p class="brand-name">leaf9tin</p>
    <p class="claim">Nur die Bohne</p>
    <p class="organic-mark">BIO</p>
  </section>
</main>
</body>
</html>
```